Business Card Design Project

We are looking for a new business card design for a Drilling company in WA, Australia.

We are in between offices, however require a design in the meantime due to some upcoming events with our basic information.

The Logo for our company is Blue and Grey and would like this colour scheme throughout.

We are quite a new company so would like a memorable design that stands out and communicates a strong commitment to safety, quality of work and performance.

The company name is Ironbark Boring Group (IBG)

The details to be included are as follows:

Gavin Thorley
Managing Director
m.0481639207
e.gavin@ibgpty.com.au

Martin Thorley
Director
m.0419852637
e.martin@ibgpty.com.au

Industry/Entity Type

Events

Requirements
Must have
• Under the Logo, we would like 'Western Australia'

```html
<!DOCTYPE html>
<html lang="en">
<head>
<meta charset="utf-8">
<title>Ironbark Boring Group – Business Card</title>
<link rel="stylesheet" href="https://fonts.googleapis.com/css2?family=PT+Sans:wght@400;700&display=swap">
<style>
  :root {
    --backdrop: #e4e2df;
    --card: #000000;
    --brand-blue: #1f4fa0;
    --contact-blue: #2f62c0;
    --brand-grey: #a7a9ac;
    --text-grey: #8d8f92;
    --shadow: rgba(0,0,0,0.35);
  }
  * { margin: 0; padding: 0; box-sizing: border-box; }
  html, body {
    width: 1200px; height: 1161px; overflow: hidden;
    background: var(--backdrop);
    font-family: "PT Sans", Arial, sans-serif;
  }
  .card {
    position: absolute;
    left: 222px;
    width: 740px; height: 434px;
    background: var(--card);
    box-shadow: 6px 10px 22px var(--shadow);
    overflow: hidden;
  }
  .card--front { top: 112px; }
  .card--back { top: 661px; }

  /* Front */
  .brand {
    position: absolute; left: 126px; top: 150px;
    display: flex; align-items: center;
  }
  .brand__initials {
    font-size: 112px; font-weight: 700; line-height: 1;
    color: var(--brand-blue); letter-spacing: -2px;
  }
  .brand__divider {
    width: 3px; height: 88px; background: var(--brand-grey);
    margin: 0 18px 0 22px;
  }
  .brand__name {
    font-size: 30px; font-weight: 700; line-height: 30px;
    text-transform: uppercase; color: var(--brand-grey);
  }
  .brand__region {
    position: absolute; left: 312px; top: 264px;
    font-size: 25px; color: var(--brand-blue); letter-spacing: 0.5px;
  }

  /* Back */
  .pattern-band { position: absolute; left: 0; top: 0; }
  .rotated {
    position: absolute; white-space: nowrap; line-height: 1;
    transform: rotate(-25deg); transform-origin: left bottom;
  }
  .back-region { left: 172px; top: 218px; font-size: 20px; color: var(--contact-blue); }
  .contact-name { left: 374px; top: 267px; font-size: 31px; color: var(--contact-blue); }
  .contact-role { left: 396px; top: 317px; font-size: 35px; color: var(--text-grey); }
  .contact-line { font-size: 18px; color: var(--contact-blue); }
  .contact-mobile { left: 420px; top: 362px; }
  .contact-email { left: 430px; top: 386px; }
</style>
</head>
<body>
  <section class="card card--front">
    <div class="brand">
      <span class="brand__initials">IBG</span>
      <span class="brand__divider"></span>
      <span class="brand__name">Ironbark<br>Boring<br>Group</span>
    </div>
    <p class="brand__region">Western Australia</p>
  </section>

  <section class="card card--back">
    <svg class="pattern-band" width="740" height="434" viewBox="0 0 740 434"
         role="img" aria-label="Diagonal band of repeated company name lettering in blue and grey">
      <defs>
        <linearGradient id="bandTone" x1="0" y1="0" x2="1" y2="1">
          <stop offset="0" stop-color="#5d6066"/>
          <stop offset="0.45" stop-color="#2c4f8c"/>
          <stop offset="1" stop-color="#3f4145"/>
        </linearGradient>
      </defs>
      <polygon points="0,0 640,0 0,290" fill="url(#bandTone)"/>
    </svg>
    <p class="rotated back-region">Western Australia</p>
    <p class="rotated contact-name">Gavin Thorley</p>
    <p class="rotated contact-role">Managing Director</p>
    <p class="rotated contact-line contact-mobile">m:0481639207</p>
    <p class="rotated contact-line contact-email">e:gavin@ibgpty.com.au</p>
  </section>
</body>
</html>
```